Consultant Firm Marketing Flyer

I want to use this flyer to market health care consultant services. I would like a front and back glossy, professional, yet bold and eye catching design. I would like it to convey knowledge, expertise, partnership and strength. The colors should blue and white but I am very open to the designer being creative. You can visit my website to see colors and images I want to use at brightmeadowadvisory.com
I would like the home page image on my website to be incorporated into the flyer but I am also open to other images that work with the design. The designer can be creative.

I want to highlight 4 service area’s of focus to my clients:
1. Revenue Cycle Optimization (making my clients money)
2. Practice Management Optimization (improving clinical operations)
3. Health Compliance (following the law)
4. Health Care Technology: (Telemedicine and AI)
Please be creative. Go where ever your creativity leads.

```html
<!DOCTYPE html>
<html lang="en">
<head>
<meta charset="utf-8">
<title>Bright Meadow Advisory – Flyer</title>
<link href="https://fonts.googleapis.com/css2?family=Roboto:wght@300;400;500;700;900&display=swap" rel="stylesheet">
<style>
:root{
  --navy:#0a3a73;
  --blue:#1478c8;
  --sky:#4cb4e8;
  --light-blue:#1f8fd6;
  --text:#555a60;
  --panel:#ececec;
  --panel-alt:#f4f4f4;
  --stage:#e8e8e8;
  --white:#ffffff;
}
*{margin:0;padding:0;box-sizing:border-box}
html,body{width:678px;height:1200px;overflow:hidden}
body{background:var(--stage);font-family:"Roboto",Arial,sans-serif;position:relative}
.page{position:absolute;left:133px;width:562px;height:790px;background:var(--white);transform:scale(0.7342);transform-origin:top left;overflow:hidden;box-shadow:0 2px 8px rgba(0,0,0,.18)}
.page--front{top:10px}
.page--back{top:610px}

/* front */
.hero{position:absolute;left:0;top:0;width:562px;height:360px;background:linear-gradient(100deg,#f3f5f8 0%,#dfe6ee 30%,#c9d3de 55%,#8c96a6 75%,#eef1f4 100%)}
.brand{position:absolute;left:22px;top:40px;color:var(--navy);font-weight:500;font-size:15px;letter-spacing:.3px}
.brand small{display:block;font-size:15px}
.headline-box{position:absolute;left:0;top:118px;width:222px;height:136px;background:rgba(76,180,232,.9);padding:12px 16px 0 28px}
.headline-box .thin{font-weight:300;font-size:21px;color:var(--navy);letter-spacing:1px;line-height:1.05}
.headline-box .bold{font-weight:900;font-size:24px;color:var(--navy);line-height:1.05}
.headline-box .light{font-weight:400;font-size:23px;color:var(--white);letter-spacing:1px;line-height:1.05}
.headline-box p{font-size:6px;color:var(--white);line-height:1.3;margin-top:3px;text-align:justify}
.swoosh{position:absolute;left:0;top:270px}
.intro{position:absolute;top:368px;font-size:8.3px;line-height:1.3;color:var(--text);text-align:justify}
.intro--welcome{left:28px;width:238px}
.intro--about{left:288px;width:245px}
.intro h2{font-size:12.5px;line-height:1.15;margin-bottom:4px;font-weight:700;text-transform:uppercase}
.intro h2 span{display:block;color:var(--light-blue)}
.intro h2 b{color:var(--navy)}
.footer-band{position:absolute;left:0;right:0;bottom:0;background:var(--navy)}
.page--front .footer-band{height:65px}
.solutions{position:absolute;left:28px;top:535px;width:506px;height:197px;display:flex}
.solution{flex:1;background:var(--panel);text-align:center;padding:30px 8px 0;color:var(--text)}
.solution:nth-child(even){background:var(--panel-alt)}
.solution h3{font-size:10px;color:var(--blue);line-height:1.2;margin-top:6px}
.solution .tag{font-size:5.8px;margin:3px 0 5px}
.solution p{font-size:5.8px;line-height:1.3}
.solutions-tab{position:absolute;left:52px;top:518px;background:var(--navy);color:var(--white);font-weight:500;font-size:12px;padding:4px 8px;z-index:2}
.icon-ring{display:block;margin:0 auto}
.contact{position:absolute;left:0;right:0;bottom:0;height:52px;display:flex;justify-content:center;align-items:center;gap:8px;color:var(--white);font-size:11px;font-weight:500}
.contact .sep{width:1px;height:13px;background:rgba(255,255,255,.6)}
.contact svg{vertical-align:-2px;margin-right:4px}

/* back */
.service{position:absolute;width:240px;font-size:8px;line-height:1.27;color:var(--text);text-align:justify}
.service header{display:flex;align-items:center;gap:10px;margin-bottom:12px}
.service h3{font-size:10px;line-height:1.2;color:var(--light-blue);font-weight:700;text-transform:uppercase}
.service h3.title-case{text-transform:none}
.service p{margin-bottom:6px}
.checks{list-style:none;margin:4px 0 8px}
.checks li{position:relative;padding-left:14px;font-weight:500;color:#333;margin-bottom:2.5px;text-align:justify}
.checks li::before{content:"✓";position:absolute;left:0;top:0.5px;width:8px;height:8px;border-radius:50%;background:var(--navy);color:var(--white);font-size:6px;line-height:8px;text-align:center;font-weight:700}
.back-photo{position:absolute;left:270px;top:600px;width:292px;height:148px;background:linear-gradient(90deg,rgba(255,255,255,1) 0%,#dde4ec 25%,#b8c3d0 55%,#e6ebf0 100%)}
.page--back .footer-band{height:44px}
.page--back .contact{height:44px}
</style>
</head>
<body>

<section class="page page--front">
  <div class="hero" role="img" aria-label="Photo of a team of doctors and consultants meeting around a bright office table"></div>
  <div class="brand">Bright Meadow Advisory LLC</div>
  <div class="headline-box">
    <div class="thin">ADVANCING</div>
    <div class="bold">HEALTHCARE</div>
    <div class="light">OPERATIONS</div>
    <p>Bright Meadow Advisory (BMA) is a healthcare consulting firm skilled at helping physician practices advance their strategic vision in an ever-evolving healthcare system.</p>
  </div>
  <svg class="swoosh" width="562" height="100" viewBox="0 0 562 100" aria-hidden="true">
    <path d="M0 98 Q260 20 562 40 L562 100 L0 100 Z" fill="#ffffff"/>
    <path d="M0 84 Q260 10 562 30" fill="none" stroke="#0a3a73" stroke-width="6"/>
    <path d="M0 92 Q260 18 562 37" fill="none" stroke="#1f8fd6" stroke-width="3"/>
  </svg>

  <div class="intro intro--welcome">
    <h2><span>Welcome to</span><b>Bright Meadow Advisory</b></h2>
    <p>Bright Meadow Advisory (BMA) is a healthcare consulting firm skilled at helping physician practices advance their strategic vision in an ever-evolving healthcare system. Bright Meadow Advisory specializes in revenue cycle optimization, practice management improvement and developing new physician practices. Our technical skills allow us to dig deep into your revenue cycle while our strategic approach ensures we're keeping our eyes on the entire financial picture.</p>
  </div>
  <div class="intro intro--about">
    <h2><span>About</span><b>Our Company</b></h2>
    <p>By implementing a comprehensive approach to optimization and working closely with your people, processes, and technology, we develop a complete picture of your organization's performance. More importantly, we're able to design strategies and solutions that improve this performance while also preserving your organization's mission, vision, and strategic initiatives. The varied expertise of our team encompass full service revenue cycle management full spectrum health care consulting services.</p>
  </div>

  <div class="footer-band"></div>
  <div class="solutions-tab">OUR SOLUTIONS</div>
  <div class="solutions">
    <div class="solution">
      <svg class="icon-ring" width="40" height="40" viewBox="0 0 40 40" aria-hidden="true"><circle cx="20" cy="20" r="18" fill="#fff" stroke="#4cb4e8" stroke-width="3"/><path d="M13 20a7 7 0 0 1 12-5M27 20a7 7 0 0 1-12 5" fill="none" stroke="#8a949e" stroke-width="2"/><path d="M25 11v4h-4M15 29v-4h4" fill="none" stroke="#8a949e" stroke-width="2"/></svg>
      <h3>Revenue<br>Cycle Optimization</h3>
      <div class="tag">making my clients money</div>
      <p>In today's increasingly complex health care environment it's important now more than ever that medical practices closely manage their revenue cycle. Bright Meadow Advisory (BMA) understands the reimbursement landscape</p>
    </div>
    <div class="solution">
      <svg class="icon-ring" width="40" height="40" viewBox="0 0 40 40" aria-hidden="true"><circle cx="20" cy="20" r="18" fill="#fff" stroke="#4cb4e8" stroke-width="3"/><circle cx="20" cy="17" r="6" fill="none" stroke="#8a949e" stroke-width="2"/><path d="M11 28h18" stroke="#8a949e" stroke-width="2"/></svg>
      <h3>Practice Management<br>Optimization</h3>
      <div class="tag">improving clinical operations</div>
      <p>Practice Management is challenging and it requires the right balance of skill, knowledge, experience and management expertise. BMA Offers assessment and optimization in Patient Access &amp; Scheduling, Patient Experience, Staff Experience</p>
    </div>
    <div class="solution">
      <svg class="icon-ring" width="40" height="40" viewBox="0 0 40 40" aria-hidden="true"><circle cx="20" cy="20" r="18" fill="#fff" stroke="#4cb4e8" stroke-width="3"/><rect x="13" y="11" width="14" height="18" rx="1" fill="none" stroke="#8a949e" stroke-width="2"/><path d="M16 20l3 3 5-6" fill="none" stroke="#8a949e" stroke-width="2"/></svg>
      <h3>Health<br>Compliance</h3>
      <div class="tag">following the law</div>
      <p>In a heavily regulated healthcare environment medical practices need to be acutely aware of regulations as they present huge liabilities. It is extremely important to ensure compliance with regulations. BMA offers a host of comprehensive compliance services</p>
    </div>
    <div class="solution">
      <svg class="icon-ring" width="40" height="40" viewBox="0 0 40 40" aria-hidden="true"><circle cx="20" cy="20" r="18" fill="#fff" stroke="#4cb4e8" stroke-width="3"/><circle cx="20" cy="16" r="5" fill="none" stroke="#8a949e" stroke-width="2"/><path d="M11 24q4 6 9 4q5 2 9-4" fill="none" stroke="#8a949e" stroke-width="2"/></svg>
      <h3>Health Care<br>Technology</h3>
      <div class="tag">Telemedicine and AI</div>
      <p>Do you need Human Resources Management but don't want the expense of a full service Human Resources Department? Not having a full service Human Resources Department can increase liability and be costly to your medical practice</p>
    </div>
  </div>
  <div class="contact">
    <span><svg width="11" height="11" viewBox="0 0 12 12" aria-hidden="true"><path d="M2 1l2 0 1 3-1.5 1a7 7 0 0 0 3.5 3.5L8 7l3 1v2a1 1 0 0 1-1 1A9 9 0 0 1 1 2a1 1 0 0 1 1-1z" fill="#4cb4e8"/></svg>(555) 214-0387</span>
    <span class="sep"></span>
    <span><svg width="12" height="9" viewBox="0 0 12 9" aria-hidden="true"><rect width="12" height="9" fill="#4cb4e8"/><path d="M0 0l6 5 6-5" fill="none" stroke="#0a3a73"/></svg>Info@brightmeadowadvisory.com</span>
    <span class="sep"></span>
    <span><svg width="11" height="11" viewBox="0 0 12 12" aria-hidden="true"><circle cx="6" cy="6" r="5.5" fill="none" stroke="#4cb4e8"/><path d="M0.5 6h11M6 0.5v11M2 3h8M2 9h8" stroke="#4cb4e8" stroke-width=".8"/></svg>www.brightmeadowadvisory.com</span>
  </div>
</section>

<section class="page page--back">
  <article class="service" style="left:30px;top:32px">
    <header>
      <svg width="44" height="44" viewBox="0 0 44 44" aria-hidden="true"><circle cx="22" cy="22" r="20" fill="#fff" stroke="#0a3a73" stroke-width="3"/><path d="M15 22a7 7 0 0 1 12-5M29 22a7 7 0 0 1-12 5" fill="none" stroke="#8a949e" stroke-width="2"/></svg>
      <h3>Revenue<br>Cycle Management</h3>
    </header>
    <p>In today's increasingly complex health care environment it's important now more than ever that medical practices closely manage their revenue cycle. Bright Meadow Advisory understands the reimbursement landscape and is skilled in helping medical practices maximize reimbursement. We offer a comprehensive package of revenue cycle services including:</p>
    <ul class="checks">
      <li>Medical Billing &amp; Coding</li>
      <li>Documentation &amp; Coding Audit</li>
      <li>A/R Management</li>
      <li>Dedicated Remote Billing Manager</li>
      <li>Dedicated Phone Number for Patients to Call</li>
      <li>Revenue Cycle Training for Practice Staff Monthly Reports</li>
      <li>Patient Access Assessment &amp; Optimization</li>
    </ul>
    <p>We offer each of these services individually or as part of a comprehensive bundled package.</p>
  </article>

  <article class="service" style="left:30px;top:330px">
    <header>
      <svg width="44" height="44" viewBox="0 0 44 44" aria-hidden="true"><circle cx="22" cy="22" r="20" fill="#fff" stroke="#0a3a73" stroke-width="3"/><rect x="15" y="13" width="14" height="18" rx="1" fill="none" stroke="#8a949e" stroke-width="2"/><path d="M18 22l3 3 5-6" fill="none" stroke="#8a949e" stroke-width="2"/></svg>
      <h3 class="title-case">Health<br>Compliance</h3>
    </header>
    <p>In a heavily regulated healthcare environment medical practices need to be acutely aware of regulations as they present huge liabilities. It is extremely important to ensure compliance with regulations including:</p>
    <ul class="checks">
      <li>Medical Coding Regulations</li>
      <li>False Claims Act</li>
      <li>HIPPA Privacy &amp; Security Rules</li>
      <li>Emergency Medical Treatment and Active Labor Act (EMTALA)</li>
      <li>Stark Law &amp; Anti-Kickback Statue</li>
      <li>Occupational Safety &amp; Health Administration Guidelines (OSHA)</li>
    </ul>
    <p>BMA offers a host of comprehensive compliance services. Practices have the option of completely outsourcing all compliance matters. BMA will become your full service compliance department providing:</p>
    <ul class="checks">
      <li>A Dedicated Compliance Officer</li>
      <li>Dedicated Hotline &amp; Email for Compliance Reporting</li>
      <li>Annual Work Plan &amp; Risk Assessment</li>
      <li>Compliance Training</li>
      <li>Medical Documentation Audits</li>
      <li>Compliance Plan</li>
      <li>Compliance with Safety Procedures</li>
      <li>Staff Training</li>
    </ul>
    <p>We offer each of these services individually or as part of a comprehensive bundled package.</p>
  </article>

  <article class="service" style="left:295px;top:32px">
    <header>
      <svg width="44" height="44" viewBox="0 0 44 44" aria-hidden="true"><circle cx="22" cy="22" r="20" fill="#fff" stroke="#0a3a73" stroke-width="3"/><circle cx="22" cy="19" r="6" fill="none" stroke="#8a949e" stroke-width="2"/><path d="M13 30h18" stroke="#8a949e" stroke-width="2"/></svg>
      <h3>Practice<br>Management Optimization</h3>
    </header>
    <p>Do you need Human Resources Management but don't want the expense of a full service Human Resources Department?</p>
    <p>Not having a full service Human Resources Department can increase liability and be costly to your medical practice. Let BMA become your full service HR Department. Our Services include:</p>
    <ul class="checks">
      <li>A dedicated HR Manager</li>
      <li>Development of HR Policies and Procedures</li>
      <li>Employer Coaching and Guidance</li>
      <li>Assistance with Onboarding &amp; Terminations</li>
      <li>Compensation Compliance</li>
      <li>Navigation of Complex Labor Laws Staff Training</li>
      <li>Staff Recruitment &amp; Talent Acquisition</li>
      <li>Pre-hire background checks</li>
      <li>Compliance Services: Affirmative Action, Fair labor Standards Act (FLSA) Compliance audit, FMLA &amp; Much More.</li>
    </ul>
    <p>These services can be purchased individually or as part of a comprehensive package.</p>
  </article>

  <article class="service" style="left:295px;top:372px">
    <header>
      <svg width="44" height="44" viewBox="0 0 44 44" aria-hidden="true"><circle cx="22" cy="22" r="20" fill="#fff" stroke="#0a3a73" stroke-width="3"/><circle cx="22" cy="18" r="5" fill="none" stroke="#8a949e" stroke-width="2"/><path d="M13 26q4 6 9 4q5 2 9-4" fill="none" stroke="#8a949e" stroke-width="2"/></svg>
      <h3>Health Care<br>Technology</h3>
    </header>
    <p>Practice Management is challenging and it requires the right balance of skill, knowledge, experience and management expertise. BMA Offers assessment and optimization in the following areas:</p>
    <ul class="checks">
      <li>Patient Access &amp; Scheduling</li>
      <li>Patient Experience</li>
      <li>Staff Experience</li>
      <li>Online Reputation Management</li>
      <li>Strategic Planning</li>
    </ul>
    <p>We offer each of these services individually or as part of a comprehensive bundled package.</p>
  </article>

  <div class="back-photo" role="img" aria-label="Photo of two business consultants reviewing reports at a laptop"></div>
  <div class="footer-band"></div>
  <div class="contact">
    <span><svg width="11" height="11" viewBox="0 0 12 12" aria-hidden="true"><path d="M2 1l2 0 1 3-1.5 1a7 7 0 0 0 3.5 3.5L8 7l3 1v2a1 1 0 0 1-1 1A9 9 0 0 1 1 2a1 1 0 0 1 1-1z" fill="#4cb4e8"/></svg>(555) 214-0387</span>
    <span class="sep"></span>
    <span><svg width="12" height="9" viewBox="0 0 12 9" aria-hidden="true"><rect width="12" height="9" fill="#4cb4e8"/><path d="M0 0l6 5 6-5" fill="none" stroke="#0a3a73"/></svg>Info@brightmeadowadvisory.com</span>
    <span class="sep"></span>
    <span><svg width="11" height="11" viewBox="0 0 12 12" aria-hidden="true"><circle cx="6" cy="6" r="5.5" fill="none" stroke="#4cb4e8"/><path d="M0.5 6h11M6 0.5v11M2 3h8M2 9h8" stroke="#4cb4e8" stroke-width=".8"/></svg>www.brightmeadowadvisory.com</span>
  </div>
</section>

</body>
</html>
```